quorVale - website to pay membership association fee

The main purpose of this site it to allow a pre-registered user to be able to view the membership fees for their membership association and pay the same in one of the ways offered by the portal.
You are required to create a graphical project only for the logon functions as a user, while omitting the back end/administration ones that will be decided later
The site, besides being responsive must be very intuitive in its function. The graphics must be bright.

Number of Pages Required

4 page

Requirements
Must have
• i need to see template for
• 1. Home page
• 2. Page after login. People can se one or more bill to Pay and decide to see more details or to pay.
• 3. Page to Pay. Choose the desired payment method five alternative

```html
<!DOCTYPE html>
<html lang="en">
<head>
<meta charset="utf-8">
<title>quorVale – Bills</title>
<link rel="stylesheet" href="https://fonts.googleapis.com/css2?family=Lato:wght@400;700;900&display=swap">
<style>
  :root {
    --brand-blue: #0563c9;
    --sky: #5cc2f4;
    --alert-orange: #f26522;
    --paid-green: #12a663;
    --page-bg: #e0e0e5;
    --card-open: #d5d5d8;
    --card-closed: #c4c4c4;
    --ink: #3a3a3a;
    --white: #ffffff;
  }
  * { box-sizing: border-box; margin: 0; padding: 0; }
  html, body { width: 1200px; height: 714px; overflow: hidden; }
  body { font-family: "Lato", sans-serif; background: var(--page-bg); position: relative; }

  .backdrop { position: absolute; left: 265px; top: 0; width: 935px; height: 714px; }

  .sidebar { position: absolute; left: 0; top: 0; width: 265px; height: 714px; background: var(--brand-blue); color: var(--white); }
  .brand { position: absolute; left: 13px; top: 8px; font-size: 37px; font-weight: 400; letter-spacing: 0.5px; }
  .nav-item { position: absolute; display: flex; align-items: center; }
  .nav-all { left: 7px; top: 136px; font-size: 23px; }
  .nav-all .caret { width: 16px; height: 14px; margin-right: 12px; }
  .nav-sub { left: 33px; font-size: 18px; }
  .nav-unpaid { top: 173px; }
  .nav-paid { top: 200px; }
  .count { position: absolute; color: var(--white); display: flex; align-items: center; justify-content: center; }
  .count-all { left: 198px; top: 139px; width: 50px; height: 23px; border-radius: 6px; background: var(--sky); font-size: 19px; }
  .count-unpaid { left: 220px; top: 173px; width: 24px; height: 24px; border-radius: 50%; background: var(--alert-orange); font-size: 15px; }
  .count-paid { left: 220px; top: 201px; width: 24px; height: 24px; border-radius: 50%; background: var(--paid-green); font-size: 15px; }

  .page-title { position: absolute; left: 301px; top: 14px; font-size: 37px; font-weight: 700; color: var(--brand-blue); }
  .logoff { position: absolute; left: 1081px; top: 13px; width: 97px; height: 38px; background: var(--white); display: flex; align-items: center; justify-content: center; font-size: 9px; font-weight: 700; color: #222; }

  .bill { position: absolute; left: 312px; width: 858px; border-radius: 10px; box-shadow: 0 3px 4px rgba(0,0,0,0.18); }
  .bill-open { left: 310px; width: 860px; top: 162px; height: 292px; background: var(--card-open); }
  .bill-closed { background: var(--card-closed); height: 69px; }
  .bill-14 { top: 478px; }
  .bill-13 { top: 572px; }
  .bill-12 { top: 662px; }
  .bill-name { position: absolute; left: 19px; font-size: 20px; font-weight: 400; }
  .bill-open .bill-name { top: 13px; color: var(--brand-blue); }
  .bill-closed .bill-name { top: 22px; color: #f4f4f4; }
  .bill-12 .bill-name { top: 19px; }

  .btn { position: absolute; display: flex; align-items: center; justify-content: center; border-radius: 5px; color: var(--white); font-size: 15px; }
  .btn-details { width: 169px; height: 38px; background: var(--brand-blue); border: 1px solid #0350a8; }
  .btn-details svg { width: 13px; height: 11px; margin-right: 17px; }
  .btn-pay { width: 76px; height: 38px; background: var(--alert-orange); border: 1px solid #c8501a; }
  .btn-paid { width: 76px; height: 38px; background: var(--paid-green); }

  .detail-row { position: absolute; left: 38px; width: 364px; height: 30px; display: flex; align-items: center; color: var(--ink); }
  .detail-row .label { white-space: nowrap; }
  .detail-row .leader { flex: 1; height: 1px; border-bottom: 1px dotted #555; margin: 8px 0 0 2px; }
  .row-fee { top: 80px; font-size: 13px; font-weight: 700; }
  .row-due { top: 121px; font-size: 12px; }
  .value { position: absolute; left: 409px; height: 30px; border-radius: 5px; background: var(--brand-blue); color: var(--white); font-weight: 700; font-size: 13px; display: flex; align-items: center; justify-content: center; }
  .value-fee { top: 80px; width: 111px; font-size: 14px; }
  .value-due { top: 121px; width: 161px; }
  .association-mark { position: absolute; left: 48px; top: 199px; font-size: 46px; line-height: 56px; font-weight: 900; color: var(--brand-blue); letter-spacing: 2px; }
  .read-more { position: absolute; left: 660px; top: 251px; font-size: 15px; color: var(--brand-blue); text-decoration: underline; }
</style>
</head>
<body>
  <svg class="backdrop" viewBox="0 0 935 714" aria-hidden="true">
    <g fill="none" stroke="#ebebef" stroke-width="1.5">
      <circle cx="560" cy="1050" r="950"/>
      <circle cx="560" cy="1050" r="820"/>
      <circle cx="560" cy="1050" r="1100"/>
    </g>
  </svg>

  <nav class="sidebar">
    <div class="brand">quorVale</div>
    <div class="nav-item nav-all">
      <svg class="caret" viewBox="0 0 16 14"><polygon points="0,0 16,0 8,14" fill="#fff"/></svg>All Bills
    </div>
    <div class="count count-all">15</div>
    <div class="nav-item nav-sub nav-unpaid">-Non-Paid</div>
    <div class="count count-unpaid">3</div>
    <div class="nav-item nav-sub nav-paid">-Paid</div>
    <div class="count count-paid">12</div>
  </nav>

  <h1 class="page-title">BILLS</h1>
  <div class="logoff">LOG OFF</div>

  <section class="bill bill-open">
    <h2 class="bill-name">BILL NUMBER 15</h2>
    <div class="btn btn-details" style="left:669px;top:13px;">
      <svg viewBox="0 0 13 11"><polygon points="6.5,0 13,11 0,11" fill="#fff"/></svg>HIDE DETAILS
    </div>
    <div class="detail-row row-fee"><span class="label">MEMBERSHIP 2017/09</span><span class="leader"></span></div>
    <div class="value value-fee">150$</div>
    <div class="detail-row row-due"><span class="label">DUE ON</span><span class="leader"></span></div>
    <div class="value value-due">DECEMBER 24</div>
    <div class="association-mark">LOGO HERE</div>
    <a class="read-more">READ MORE</a>
    <div class="btn btn-pay" style="left:762px;top:242px;">PAY</div>
  </section>

  <section class="bill bill-closed bill-14">
    <h2 class="bill-name">BILL NUMBER 14</h2>
    <div class="btn btn-pay" style="left:571px;top:19px;">PAY</div>
    <div class="btn btn-details" style="left:667px;top:19px;">
      <svg viewBox="0 0 13 11"><polygon points="0,0 13,0 6.5,11" fill="#fff"/></svg>SHOW DETAILS
    </div>
  </section>

  <section class="bill bill-closed bill-13">
    <h2 class="bill-name">BILL NUMBER 13</h2>
    <div class="btn btn-pay" style="left:571px;top:15px;">PAY</div>
    <div class="btn btn-details" style="left:667px;top:15px;">
      <svg viewBox="0 0 13 11"><polygon points="0,0 13,0 6.5,11" fill="#fff"/></svg>SHOW DETAILS
    </div>
  </section>

  <section class="bill bill-closed bill-12">
    <h2 class="bill-name">BILL NUMBER 12</h2>
    <div class="btn btn-paid" style="left:571px;top:14px;">PAID</div>
    <div class="btn btn-details" style="left:667px;top:14px;">
      <svg viewBox="0 0 13 11"><polygon points="0,0 13,0 6.5,11" fill="#fff"/></svg>SHOW DETAILS
    </div>
  </section>
</body>
</html>
```